Graphic Design for a Info Card

We would like a graphic design for an info card . We would like the colours to correspond to our logo , you can add in the colours navy blue or yellow if you would like. We would like it to have the following information. We want something that really pops. We would like the size to be 4 1/2 x 6 .

ATTENTION!! Delivery Promo! Order from us on the @hopplemeals app or @marlinrunner app on FRIDAYS and receive a FREE Sample of our one of our meal prep meals in your bag!
DID YOU KNOW?! Meal Prep is another great service that we offer. Saving you time, promoting your health, and best of all providing a delicious lunch . You can find more info on our website www.brivoranpantry.example . All orders are available for delivery or pickup!

```html
<!DOCTYPE html>
<html lang="en">
<head>
<meta charset="utf-8">
<title>Brivoran Delivery Promo Card</title>
<link rel="stylesheet" href="https://fonts.googleapis.com/css2?family=Bebas+Neue&family=Oswald:wght@700&family=Montserrat:wght@500;700;800&family=Open+Sans:ital,wght@1,700;1,800&display=swap">
<style>
  :root {
    --navy: #1a3d70;
    --navy-deep: #17345f;
    --teal: #1482ad;
    --yellow: #fdd319;
    --yellow-deep: #f9b91c;
    --red: #e31d2a;
    --wine: #5a0a2a;
    --green: #8cc63f;
    --white: #ffffff;
    --ink: #0f2c55;
    --stage: #eeeeee;
  }
  * { margin: 0; padding: 0; box-sizing: border-box; }
  html, body { width: 1200px; height: 1200px; overflow: hidden; background: var(--stage); }
  .card {
    position: absolute; left: 196px; top: 60px; width: 808px; height: 1078px;
    background: linear-gradient(135deg, var(--navy-deep) 0%, var(--navy) 40%, var(--teal) 100%);
    overflow: hidden;
    font-family: "Montserrat", sans-serif;
  }
  .light-beam {
    position: absolute; inset: 0;
    background: linear-gradient(120deg, transparent 48%, rgba(40,150,200,0.35) 70%, transparent 100%);
  }
  .burst { position: absolute; left: 440px; top: 0; width: 368px; height: 270px; }
  .promo-label {
    position: absolute; left: 585px; top: 60px; width: 240px;
    font-family: "Montserrat", sans-serif; font-weight: 800; font-size: 38px; line-height: 0.95;
    color: var(--red); text-transform: uppercase; transform: rotate(28deg); text-align: center;
  }
  .brand { position: absolute; left: 34px; top: 38px; }
  .brand-name {
    font-family: "Montserrat", sans-serif; font-weight: 800; font-size: 72px; letter-spacing: 2px;
    color: #9a9a9a; line-height: 1;
  }
  .brand-tagline {
    margin-top: 6px; font-weight: 800; font-size: 23px; color: var(--green); letter-spacing: -0.3px;
  }
  .headline {
    position: absolute; left: 60px; top: 178px; white-space: nowrap;
    font-family: "Oswald", sans-serif; font-weight: 700; font-size: 168px; line-height: 1;
    color: var(--white); letter-spacing: -3px;
    transform-origin: left top; transform: skewX(-12deg) scaleX(0.86);
    text-shadow: 6px 10px 18px rgba(0,0,0,0.45);
  }
  .phone {
    position: absolute; left: 94px; top: 366px; width: 245px; height: 432px;
    background: var(--white); border-radius: 26px; box-shadow: 0 8px 20px rgba(0,0,0,0.25);
  }
  .phone-screen {
    position: absolute; left: 22px; top: 44px; width: 202px; height: 311px;
    background: linear-gradient(90deg, var(--yellow-deep), var(--yellow)); border-radius: 4px;
    text-align: center;
  }
  .pin { position: absolute; left: 49px; top: 10px; width: 104px; height: 140px; }
  .app-name { position: absolute; left: 0; width: 100%; font-weight: 700; font-size: 17px; color: var(--ink); }
  .app-handle { position: absolute; left: 0; width: 100%; font-weight: 800; font-size: 13px; color: #1b1b1b; }
  .home-button {
    position: absolute; left: 103px; top: 378px; width: 36px; height: 36px;
    border: 4px solid var(--yellow); border-radius: 50%;
  }
  .offer-frame {
    position: absolute; left: 377px; top: 380px; width: 420px; height: 150px;
    border: 1.5px solid rgba(255,255,255,0.85); transform: rotate(-2deg);
  }
  .offer-banner {
    position: absolute; left: 388px; top: 392px; width: 394px; height: 130px;
    background: linear-gradient(90deg, var(--red), var(--wine)); transform: rotate(-2deg);
    font-family: "Bebas Neue", sans-serif; font-size: 54px; line-height: 0.95; color: var(--white);
    text-align: center; padding-top: 16px; text-shadow: 2px 3px 0 rgba(0,0,0,0.35);
  }
  .sample-frame {
    position: absolute; left: 446px; top: 530px; width: 312px; height: 96px;
    border: 1.5px solid rgba(255,255,255,0.85); transform: rotate(2deg);
  }
  .sample-box {
    position: absolute; left: 456px; top: 520px; width: 298px; height: 82px;
    background: var(--white); transform: rotate(2deg);
    font-family: "Bebas Neue", sans-serif; font-size: 38px; color: #9c1530;
    text-align: center; line-height: 82px; box-shadow: 0 6px 14px rgba(0,0,0,0.25);
  }
  .pointer-arrow { position: absolute; left: 340px; top: 590px; width: 160px; height: 70px; }
  .know-title {
    position: absolute; left: 392px; top: 668px; white-space: nowrap;
    font-family: "Oswald", sans-serif; font-weight: 700; font-size: 72px; line-height: 1;
    color: var(--yellow); letter-spacing: -1px;
    transform-origin: left top; transform: skewX(-12deg) scaleX(0.88);
    text-shadow: 4px 6px 12px rgba(0,0,0,0.35);
  }
  .know-body {
    position: absolute; left: 386px; top: 752px; width: 370px;
    font-weight: 500; font-size: 21px; line-height: 25px; color: var(--white); text-align: justify;
  }
  .web-bar {
    position: absolute; left: 33px; top: 889px; width: 660px; height: 69px;
    background: linear-gradient(90deg, var(--yellow-deep), var(--yellow)); border-radius: 10px;
    font-family: "Open Sans", sans-serif; font-style: italic; font-weight: 800; font-size: 42px;
    color: var(--ink); line-height: 69px; text-align: center; letter-spacing: -0.5px; white-space: nowrap;
  }
  .tap-icon { position: absolute; left: 676px; top: 930px; width: 60px; height: 60px; }
  .fulfilment-note {
    position: absolute; left: 100px; top: 976px; width: 570px; text-align: center;
    font-family: "Open Sans", sans-serif; font-style: italic; font-weight: 800; font-size: 37px;
    line-height: 39px; color: var(--yellow); text-transform: uppercase;
  }
</style>
</head>
<body>
<main class="card">
  <div class="light-beam"></div>

  <svg class="burst" viewBox="0 0 368 270" aria-hidden="true">
    <defs>
      <linearGradient id="burstFill" x1="0" y1="0" x2="1" y2="1">
        <stop offset="0" stop-color="#f9b91c"/><stop offset="1" stop-color="#ffe51a"/>
      </linearGradient>
    </defs>
    <polygon points="155,0 368,0 368,270 330,250 320,200 280,190 262,150 215,148 225,110 170,108 190,80 130,60 185,45 140,20"
      fill="#101820"/>
    <polygon points="165,0 368,0 368,228 325,225 312,185 272,178 258,138 220,135 232,102 180,96 198,74 148,56 196,42 156,18"
      fill="url(#burstFill)"/>
  </svg>
  <div class="promo-label">Delivery<br>Promo!</div>

  <header class="brand">
    <div class="brand-name">BRIVORAN</div>
    <div class="brand-tagline">HEALTHY KITCHEN &nbsp;|&nbsp; MEAL PREP</div>
  </header>

  <h1 class="headline">ATTENTION!!</h1>

  <div class="phone">
    <div class="phone-screen">
      <svg class="pin" viewBox="0 0 104 140" role="img" aria-label="Location pin with delivery scooter icon">
        <defs>
          <linearGradient id="pinFill" x1="0" y1="0" x2="1" y2="1">
            <stop offset="0" stop-color="#1a3d70"/><stop offset="1" stop-color="#1482ad"/>
          </linearGradient>
        </defs>
        <path d="M52 4 C24 4 4 24 4 52 C4 84 52 136 52 136 C52 136 100 84 100 52 C100 24 80 4 52 4 Z" fill="url(#pinFill)"/>
        <circle cx="52" cy="52" r="38" fill="none" stroke="#fdd319" stroke-width="3"/>
        <circle cx="52" cy="52" r="32" fill="#fdd319"/>
      </svg>
      <div class="app-name" style="top:170px">Marlin Runner</div>
      <div class="app-handle" style="top:196px">@MARLINRUNNER APP</div>
      <div class="app-name" style="top:244px">Hopple Meals</div>
      <div class="app-handle" style="top:270px">@HOPPLEMEALS APP</div>
    </div>
    <div class="home-button"></div>
  </div>

  <div class="offer-frame"></div>
  <div class="offer-banner">ORDER FROM US ON<br>FRIDAYS</div>
  <div class="sample-frame"></div>
  <div class="sample-box">RECEIVE A FREE SAMPLE</div>

  <svg class="pointer-arrow" viewBox="0 0 160 70" aria-hidden="true">
    <path d="M4 8 C30 60 110 70 148 24" fill="none" stroke="#fff" stroke-width="3.5" stroke-dasharray="8 6"/>
    <path d="M132 20 L150 20 L148 40" fill="none" stroke="#fff" stroke-width="3.5"/>
  </svg>

  <h2 class="know-title">DID YOU KNOW?</h2>
  <p class="know-body">Meal Prep is another great service that we offer. Saving you time, promoting your health, and best of all providing a delicious lunch.</p>

  <div class="web-bar">www.brivoranpantry.example</div>
  <svg class="tap-icon" viewBox="0 0 60 60" aria-hidden="true">
    <path d="M8 14 a10 10 0 0 1 18 -2" fill="none" stroke="#fff" stroke-width="2.5"/>
    <path d="M16 16 L16 40 L10 34 L6 38 L20 56 L46 56 L52 38 L52 26 L44 24 L36 22 L24 20 L24 16 Z" fill="none" stroke="#fff" stroke-width="3" stroke-linejoin="round"/>
  </svg>

  <p class="fulfilment-note">All orders are available<br>for delivery or pickup!</p>
</main>
</body>
</html>
```